Gardener needs an exciting new flyer design.

I'm a passionate gardener that requires a custom flyer design for a owner operator gardening business. Design will be for a DL flyer. I'm based on the Sunshine coast in Queensland Australia. My target audience is the residential market on the Sunshine coast. Business name is Marlowe Greens. My services are, lawn mowing, weeding, Eco Friendly fertilizing, green waste removal, Mulching, tree and shrub pruning, Full garden makeovers, hedging, pressure cleaning, privacy screening, Timber deck rejuvenation, Planting, Turf preparation and installation, and much more. Free no obligation quotes, reliable and friendly service, great rates. 12 years experience. Web www.marlowegreens.com.au - Phone 0418527064 - Email doug@marlowegreens.com.au I would like the design to portray a friendly and professional approach.

Target Market(s)

Residential

Industry/Entity Type

Gardener

Font styles to use
Serif

Colors
9ccb3b
abd037
3176b5

Requirements
Must have
• my services, my logo, my contact details,

```html
<!DOCTYPE html>
<html lang="en">
<head>
<meta charset="utf-8">
<title>Marlowe Greens – DL Flyer</title>
<link rel="stylesheet" href="https://fonts.googleapis.com/css2?family=Teko:wght@500;600&family=Roboto:wght@400;500;700&display=swap">
<style>
  :root{
    --lime:#9ccb3b;
    --lime-2:#abd037;
    --blue:#3176b5;
    --ink:#2b2b2b;
    --paper:#ffffff;
    --paper-shade:#eef0ee;
    --stage:#75a12a;
    --photo-dark:#24382c;
    --photo-mid:#4f6b55;
    --photo-light:#8a97a3;
  }
  *{box-sizing:border-box;margin:0;padding:0}
  html,body{width:1200px;height:900px;overflow:hidden}
  body{background:var(--stage);font-family:"Roboto",Arial,sans-serif;color:var(--ink)}
  .flyer{
    position:absolute;left:400px;top:27px;width:400px;height:846px;
    background:linear-gradient(180deg,var(--paper) 55%,var(--paper-shade) 100%);
    overflow:hidden;box-shadow:0 18px 40px rgba(0,0,0,.25);
  }
  .hero{position:absolute;left:0;top:0;width:400px;height:500px}
  .brand-title{position:absolute;left:0;right:0;top:150px;text-align:center;
    font-family:"Teko",sans-serif;font-weight:600;line-height:.82;text-transform:uppercase}
  .brand-title .line-1{display:block;color:#fff;font-size:86px;letter-spacing:1px}
  .brand-title .line-2{display:inline-block;margin-top:4px;padding:10px 16px 0;
    background:var(--lime-2);color:#fff;font-size:86px;letter-spacing:1px}
  .services-heading{position:absolute;left:0;right:0;top:510px;text-align:center;
    font-family:"Teko",sans-serif;font-weight:600;font-size:50px;color:var(--blue);letter-spacing:.5px}
  .service-list{position:absolute;list-style:none;font-size:12.5px;line-height:1.22}
  .service-list li{position:relative;padding-left:12px}
  .service-list li::before{content:"";position:absolute;left:0;top:5px;width:6px;height:6px;background:var(--lime)}
  .service-list li.cont{padding-left:24px}
  .service-list li.cont::before{display:none}
  .list-left{left:38px;top:600px}
  .list-right{left:210px;top:568px}
  .more-badge{position:absolute;left:182px;top:686px;background:var(--blue);color:#fff;
    font-family:"Teko",sans-serif;font-weight:600;font-size:24px;line-height:1;padding:6px 14px 2px;text-transform:uppercase}
  .pitch{position:absolute;left:0;right:0;top:726px;text-align:center;font-size:13px;line-height:1.3}
  .pitch .highlight{color:var(--lime)}
  .footer{position:absolute;left:28px;right:28px;top:770px;height:50px;display:flex;align-items:center}
  .wordmark{flex:0 0 150px;display:flex;align-items:center;gap:7px;font-weight:700;font-size:15px;color:#3f8a2c}
  .wordmark .dot{width:12px;height:12px;border-radius:50%;background:#3f8a2c}
  .divider{width:1.5px;height:48px;background:#555;margin:0 14px}
  .contacts{list-style:none;font-size:11px;line-height:1.35}
  .contacts li{display:flex;align-items:center;gap:5px}
  .contacts svg{width:9px;height:9px;fill:var(--lime)}
  .base-rule{position:absolute;left:0;right:0;bottom:12px;height:2px;background:var(--lime)}
  .base-band{position:absolute;left:0;right:0;bottom:0;height:9px;background:var(--lime)}
</style>
</head>
<body>
  <main class="flyer">
    <svg class="hero" viewBox="0 0 400 500" aria-hidden="false">
      <defs>
        <linearGradient id="heroTone" x1="0" y1="0" x2="1" y2="1">
          <stop offset="0" stop-color="var(--photo-light)"/>
          <stop offset=".45" stop-color="var(--photo-mid)"/>
          <stop offset="1" stop-color="var(--photo-dark)"/>
        </linearGradient>
      </defs>
      <polygon role="img" aria-label="Photo: gardener in gloves holding a potted seedling above pots of young plants and flowers"
        points="0,0 400,0 400,410 0,480" fill="url(#heroTone)"/>
      <polygon class="chevron" points="125,452 210,468 305,426 305,442 210,486 125,470" fill="var(--lime)"/>
    </svg>

    <h1 class="brand-title"><span class="line-1">Marlowe</span><span class="line-2">Greens</span></h1>

    <h2 class="services-heading">OUR SERVICES</h2>

    <ul class="service-list list-left">
      <li>Weeding</li>
      <li>hedging</li>
      <li>pressure cleaning</li>
      <li>green waste removal</li>
      <li>Full garden makeovers</li>
      <li class="cont">Mulching, tree and</li>
      <li class="cont">shrub pruning</li>
    </ul>
    <ul class="service-list list-right">
      <li>Planting</li>
      <li>Lawn Mowing</li>
      <li>privacy screening</li>
      <li>Eco Friendly fertilizing</li>
      <li>Timber deck rejuvenation</li>
      <li>Turf preparation and</li>
      <li class="cont">installation</li>
    </ul>

    <div class="more-badge">And much more.</div>

    <p class="pitch">Free no obligation quotes, reliable and friendly<br>service, great rates. <span class="highlight">12 years experience.</span></p>

    <footer class="footer">
      <div class="wordmark"><span class="dot"></span>Marlowe Greens</div>
      <div class="divider"></div>
      <ul class="contacts">
        <li><svg viewBox="0 0 10 10"><circle cx="5" cy="5" r="5"/></svg>www.marlowegreens.com.au</li>
        <li><svg viewBox="0 0 10 10"><path d="M2 0l2 2.5-1.2 1.3a6 6 0 0 0 3.4 3.4L7.5 6 10 8l-1.5 2C4 10 0 6 0 1.5z"/></svg>0418527064</li>
        <li><svg viewBox="0 0 10 10"><path d="M0 2h10v6H0zM0 2l5 3.5L10 2" stroke="#fff" stroke-width=".8"/></svg>doug@marlowegreens.com.au</li>
      </ul>
    </footer>

    <div class="base-rule"></div>
    <div class="base-band"></div>
  </main>
</body>
</html>
```